Business Card Design for LeafSpire (Farming Devices)

We need Business Cards for our new Company based in Switzerland called "LeafSpire" We develop innovativ products for indoor and outdoor Farming for household and components for vertical farming. Our initial BloomNook gives people the possibility to grow their own food at home all year round. The design should communicate freshness, innovation, health.

```html
<!DOCTYPE html>
<html lang="en">
<head>
<meta charset="utf-8">
<title>LeafSpire Business Card</title>
<link href="https://fonts.googleapis.com/css2?family=Lato:wght@700&family=Cabin:wght@400&display=swap" rel="stylesheet">
<style>
  :root {
    --stage: #000000;
    --brand-blue: #1c60c6;
    --brand-green: #66ee00;
    --paper: #ffffff;
    --soft-green: #c0f794;
    --soft-blue: #8eafe3;
  }
  html, body {
    margin: 0;
    padding: 0;
    width: 1200px;
    height: 1200px;
    overflow: hidden;
    background: var(--stage);
  }
  .canvas {
    position: relative;
    width: 1200px;
    height: 1200px;
    background: var(--stage);
  }
  .card {
    position: absolute;
    width: 782px;
    height: 506px;
    box-sizing: border-box;
    overflow: hidden;
  }
  .card-front {
    left: 62px;
    top: 63px;
    background: var(--brand-blue);
    border: 9px solid var(--brand-green);
    display: flex;
    align-items: center;
    justify-content: center;
  }
  .wordmark {
    font-family: "Lato", sans-serif;
    font-weight: 700;
    margin: 0;
    line-height: 1;
    letter-spacing: -0.5px;
  }
  .card-front .wordmark {
    font-size: 86px;
    color: var(--paper);
    margin-top: 40px;
  }
  .card-back {
    left: 356px;
    top: 629px;
    background: var(--paper);
  }
  .backdrop {
    position: absolute;
    right: -170px;
    top: 150px;
    width: 560px;
    height: 560px;
    border-radius: 50%;
    border: 40px solid var(--soft-blue);
    box-sizing: border-box;
    opacity: 0.9;
  }
  .card-back .wordmark {
    position: absolute;
    left: 53px;
    top: 104px;
    font-size: 50px;
    color: var(--brand-blue);
  }
  .contact-list {
    position: absolute;
    left: 56px;
    top: 222px;
    margin: 0;
    padding: 0;
    list-style: none;
    font-family: "Cabin", sans-serif;
    font-size: 20px;
    letter-spacing: 1.2px;
    color: var(--brand-blue);
  }
  .contact-item {
    display: flex;
    align-items: center;
    height: 43px;
  }
  .contact-icon {
    width: 24px;
    height: 24px;
    margin-right: 24px;
    flex: none;
  }
</style>
</head>
<body>
<div class="canvas">
  <section class="card card-front">
    <h1 class="wordmark">LeafSpire</h1>
  </section>

  <section class="card card-back">
    <div class="backdrop" aria-hidden="true"></div>
    <h2 class="wordmark">LeafSpire</h2>
    <ul class="contact-list">
      <li class="contact-item">
        <svg class="contact-icon" viewBox="0 0 24 24" aria-hidden="true">
          <path d="M12 2a7 7 0 0 0-7 7c0 5 7 13 7 13s7-8 7-13a7 7 0 0 0-7-7zm0 10a3 3 0 1 1 0-6 3 3 0 0 1 0 6z" fill="var(--brand-blue)"/>
        </svg>
        <span>Xyz-building, Xyz road, Switzerland</span>
      </li>
      <li class="contact-item">
        <svg class="contact-icon" viewBox="0 0 24 24" aria-hidden="true">
          <path d="M7 3l3 4-2 2c1 3 3 5 6 6l2-2 4 3-2 4C10 20 4 14 3 5z" fill="var(--brand-blue)"/>
        </svg>
        <span>123-456-7890</span>
      </li>
      <li class="contact-item">
        <svg class="contact-icon" viewBox="0 0 24 24" aria-hidden="true">
          <rect x="1" y="5" width="22" height="14" fill="var(--brand-blue)"/>
          <path d="M1 5l11 8 11-8M1 19l8-7M23 19l-8-7" stroke="var(--paper)" stroke-width="1.4" fill="none"/>
        </svg>
        <span>leafspire@gmail.com</span>
      </li>
      <li class="contact-item">
        <svg class="contact-icon" viewBox="0 0 24 24" aria-hidden="true">
          <circle cx="12" cy="12" r="9" fill="none" stroke="var(--brand-blue)" stroke-width="2.4"/>
          <path d="M3 12h18M12 3c-4 5-4 13 0 18M12 3c4 5 4 13 0 18" stroke="var(--brand-blue)" stroke-width="1.6" fill="none"/>
        </svg>
        <span>www.leafspire.com</span>
      </li>
    </ul>
  </section>
</div>
</body>
</html>
```